Trekvilo adventure tourism social site

I require a website to be made with some custom functionality on WORDPRESS. It needs to looks simple, be optimized with the least amount of errors on it for seo, have all links work, and be MOBILE FRIENDLY! My company will be providing valuable information to extreme adventurers around the world. We will have reviews and bookings of adventures, adventure ideas,and more on the site. I want to be able to create a community within the site so that people may communicate. I have a list of wordpress plugins I believe may work well for this. I want people to be able to create their own itineraries or use one of my custom itineraries. I will be offering Trekvilo tours that we will be offering direct to customer as well. I want adventure companies to be able to create a profile for themselves that we can accept or decline and I want to be able to add many companies at a time through an excel spreadsheet full of information such as company name, phone etc.
I will be offering advertizing opportunities to some companies that have a high safety ranking and review. their adds will pop up first for the area that the adventurer chooses.

So all in all the functionality that I require is
1. I want to be able to sell advertising spots to tour companies and adventure companies and for them to have a profile on the site.
2. I need a custom form designed for these companies with pictures, reviews and information.
3. I want to provide quality information to users about these companies.
4. I want to have 2 first page ad opportunities available
5. I want the funtionality to be super simple.
6. After sign in I want a my itinerary section, favorite section that integrate with the custom form designed.
7. I would like a really simple blog section to add pics, video and more
8 I want a why trekvilo section on first page
9.I would like some sort of social network (kinloop hub) built in for usersto communicate or chat with each other.

Some features similar to the wandermapper website. but specializing in adventure tourism.

Target Market(s)

Adventure companies, tour companies, and all individual travellers that want to go on an adventure

Industry/Entity Type

Tourism

Coding

Coded - Design and coding required

Number of Pages Required

5+ page

Font styles to use
Serif
Sans Serif

Colors
ffffff
0492cd
9bcb3b

Requirements
Must have
• Wordpress, Mobile friendly, sign in, e commerce to take payment from advertisers, e commerce to take payments from people that are booking.
• Main page must have search functionality by adventure and location City, coutry, state.
• -Custom clipwall style search tiles that take you to another page
• -All plugin for social media at bottom of every page and like buttons for social media at the top of every page small in the corner.
• -Blog that integrates well with zorbit
• -Sign in option that adds extra functionality such as my itinerary, favorites section,
• - my profile section
• -Book now
• -Favorite heart that will send favorites to favorite section.
• - Wordpress zorbit map plugin somewhere on site for maps
• -Plugin for money conversion (ex cnd, us, jpn)
• -Share buttons on all form to share to friendlane, email, v+
• - Like page symbols
• -chat plugin
• -Video integration by vid lane,
• -blog that can easily ad pics and videos
• -Custom forms for tours and companies with safety ranking etc
• Site colors will match logo that is also being design by motif throng green and blue.
• I like the use of sliders especially on page 1.
• Interface must be easy to use and look at.
• simple
• - Post otter integration (plugin)
Nice to have
• -my jounal section after sign in that saves the adventures they went on and allows the user to make notes about their experience.
• - Social network built in using a plugin (kinloophub) that will allow users to communicate and have a profile
• Below are some other ideas I did research on that might help
• 1. to be made on wordpress
• 2. Main page must have a search functionality
• 3. Main pafe with custom search tiles (clipwall style)
• 4. All plugins/widgets for social media at the bottom of every page.
• 5. Chat plugin
• 6.custom forms by fields koala plugin
• 7. Blogging tool in back end adding pictures and videos
• 8. CRM plugin in background (kinloop add on)
• 9. sign in option with extra functionality including create my itinerary
• 10. Video integration by vid lane
• 11. 1 custom form designed where I can upload multiple pictures or a company/user can upload photos.
• 12. reviews in this custom forrm
• 13. safety ranking in form (star format)
• 14. difficulty in form (star format)
• 15 share button (can be by email/friendlane) there are plugins for this.
• 16. My itinerary form created on field koala or other form creator and share button on this linking website.
• 17. I Need to be able to take payments from consumers and advertisors (automatic monthly payments). I currently use plinth tapper. I dont care what site uses although plinth is already set up
• 18. plugin for money conversion on page 1
• 19. be able to save an item by favourite.
• (heart)
• 20 favourite tab with custom form of favs
• 21.post otter integration
• 22. Journal/reflection section with saved chosen item/tour that client has done
• 23. Advertise tiles 2 on first page
• 24. legal button at bottom of every page
• 25. Advertise button at bottom
• 26. Total rank tune kit plugin
• 27. Wordpress zorbit map plugin
• 28. velocore pluging to compress photos

```html
<!DOCTYPE html>
<html lang="en">
<head>
<meta charset="utf-8">
<title>Trekvilo – Live Your Adverture</title>
<link rel="stylesheet" href="https://fonts.googleapis.com/css2?family=Open+Sans:wght@300;400;600;700&display=swap">
<style>
:root{
  --blue:#0492cd;
  --green:#9bcb3b;
  --green-dark:#86b52c;
  --white:#ffffff;
  --navy:#2e4262;
  --ink:#2a2f36;
  --grey:#5b6068;
  --dot-grey:#6d7177;
}
*{margin:0;padding:0;box-sizing:border-box}
html,body{width:1152px;height:1200px;overflow:hidden;background:var(--white)}
body{font-family:"Open Sans",Arial,sans-serif;color:var(--ink);position:relative}
.abs{position:absolute}

/* Header */
.site-header{position:absolute;left:0;top:0;width:1152px;height:126px;
  background:linear-gradient(180deg,#34496b 0%,#2b3e5e 100%)}
.menu-toggle{left:134px;top:26px;width:30px;height:22px;display:flex;flex-direction:column;justify-content:space-between}
.menu-toggle span{display:block;height:4px;background:var(--white)}
.brand{left:204px;top:50px;display:flex;align-items:center;gap:12px}
.brand-mark{width:46px;height:46px;border-radius:50%;background:var(--blue)}
.brand-name{font-size:30px;font-weight:600;color:var(--green);letter-spacing:.5px}
.account-links{left:785px;top:19px;font-size:13px;color:var(--white);display:flex;gap:12px}
.account-links .sign-in{color:var(--green)}
.social-likes{left:912px;top:25px;display:flex;gap:12px}
.social-likes span{width:11px;height:11px;border-radius:50%;background:var(--white)}
.btn{display:flex;align-items:center;justify-content:center;color:var(--white);font-weight:700;text-transform:uppercase}
.btn-shop{left:822px;top:64px;width:102px;height:33px;background:var(--green);color:var(--navy);font-size:12px;gap:7px}
.btn-book{left:930px;top:64px;width:102px;height:33px;background:var(--blue);font-size:12px}

/* Hero */
.hero{left:0;top:126px;width:1152px;height:427px;
  background:linear-gradient(180deg,#f4f8fb 0%,#e2eef3 30%,#a9c7cf 55%,#5d8a5a 72%,#3f6c34 100%)}
.hero-feature{left:840px;top:160px;width:312px;height:473px;z-index:3;
  background:linear-gradient(180deg,#b9c9d3 0%,#9a8068 40%,#7a5c42 100%)}
.hero-title{left:120px;top:258px;z-index:2}
.hero-title .lead{display:block;font-size:40px;font-weight:700;color:var(--ink);line-height:1}
.hero-title .main{display:block;font-size:76px;font-weight:700;color:var(--blue);line-height:1;margin-top:12px;letter-spacing:1px}
.slider-dots{display:flex;gap:5px}
.slider-dots span{width:13px;height:13px;border-radius:50%;background:var(--white)}
.hero-dots{left:552px;top:510px}
.hero-dots span.active{background:var(--green)}

/* Search band */
.search-band{left:0;top:553px;width:1152px;height:238px;background:var(--green)}
.search-title{left:120px;top:585px;font-size:18px;font-weight:600;color:var(--white)}
.search-rule{left:120px;top:619px;width:754px;height:1px;background:var(--green-dark)}
.field-label{top:636px;font-size:14px;color:var(--ink)}
.select{top:663px;height:44px;background:var(--white);border:1px solid #c9d6b8;display:flex;align-items:center;font-size:12px;color:var(--grey)}
.select .value{flex:1;padding-left:16px}
.select .caret{width:38px;height:100%;border-left:1px solid #c9d6b8;display:flex;align-items:center;justify-content:center}
.btn-search{left:788px;top:730px;width:166px;height:40px;background:var(--blue);font-size:16px;font-weight:600;gap:12px}

/* Adventure tiles */
.section-title{left:118px;top:834px;color:var(--blue);font-size:54px;font-weight:300;white-space:nowrap}
.section-title small{font-size:38px;color:var(--grey);font-weight:300}
.btn-join{left:744px;top:846px;width:131px;height:40px;background:var(--blue);font-size:12px;font-weight:600}
.list-toggle{left:897px;top:858px;width:35px;height:18px;display:flex;flex-direction:column;justify-content:space-between}
.list-toggle span{height:4px;background:var(--ink)}
.btn-share{left:954px;top:846px;width:78px;height:40px;background:var(--green);color:var(--ink);font-size:12px;font-weight:600}
.tile{top:952px;width:210px;height:165px}
.tile-media{height:125px}
.tile-label{height:40px;background:var(--green);font-size:12px;font-weight:700;color:var(--ink);display:flex;align-items:center;padding-left:25px;text-transform:uppercase}
.tiles-dots{left:556px;top:1150px;gap:4px}
.tiles-dots span{width:11px;height:11px;background:var(--dot-grey)}
.tiles-dots span.active{background:var(--blue)}
</style>
</head>
<body>

<header class="site-header">
  <div class="abs menu-toggle" aria-label="Menu"><span></span><span></span><span></span></div>
  <div class="abs brand"><span class="brand-mark"></span><span class="brand-name">Trekvilo</span></div>
  <nav class="abs account-links"><span>Join</span><span>I</span><span class="sign-in">Sign In</span></nav>
  <div class="abs social-likes" aria-label="Social links"><span></span><span></span><span></span><span></span><span></span><span></span></div>
  <a class="abs btn btn-shop">
    <svg width="12" height="11" viewBox="0 0 12 11"><path d="M0 1h2l2 6h6l2-5H3.5" fill="none" stroke="#2e4262" stroke-width="1.6"/><circle cx="5" cy="9.5" r="1.2" fill="#2e4262"/><circle cx="9" cy="9.5" r="1.2" fill="#2e4262"/></svg>
    Shop</a>
  <a class="abs btn btn-book">Book</a>
</header>

<section class="abs hero" role="img" aria-label="Misty forested valley under a pale sky"></section>
<div class="abs hero-feature" role="img" aria-label="Hiker with a backpack resting on a large rock outcrop"></div>
<h1 class="abs hero-title"><span class="lead">LIVE YOUR</span><span class="main">ADVERTURE</span></h1>
<div class="abs slider-dots hero-dots"><span></span><span class="active"></span><span></span></div>

<section class="abs search-band"></section>
<h2 class="abs search-title">FIND AN ADVERTURE</h2>
<div class="abs search-rule"></div>
<label class="abs field-label" style="left:120px">Find :</label>
<label class="abs field-label" style="left:511px">Near :</label>
<div class="abs select" style="left:120px;width:366px"><span class="value">Things todo</span><span class="caret"><svg width="10" height="6"><path d="M1 1l4 4 4-4" fill="none" stroke="#555" stroke-width="1.3"/></svg></span></div>
<div class="abs select" style="left:512px;width:130px"><span class="value">City</span><span class="caret"><svg width="10" height="6"><path d="M1 1l4 4 4-4" fill="none" stroke="#555" stroke-width="1.3"/></svg></span></div>
<div class="abs select" style="left:667px;width:130px"><span class="value">Country</span><span class="caret"><svg width="10" height="6"><path d="M1 1l4 4 4-4" fill="none" stroke="#555" stroke-width="1.3"/></svg></span></div>
<div class="abs select" style="left:823px;width:130px"><span class="value">State</span><span class="caret"><svg width="10" height="6"><path d="M1 1l4 4 4-4" fill="none" stroke="#555" stroke-width="1.3"/></svg></span></div>
<a class="abs btn btn-search">
  <svg width="17" height="17" viewBox="0 0 17 17"><circle cx="7" cy="7" r="5.2" fill="none" stroke="#fff" stroke-width="2.4"/><path d="M11 11l5 5" stroke="#fff" stroke-width="2.6"/></svg>
  SEARCH</a>

<h2 class="abs section-title">FIND YOUR <small>ADVERTURE</small></h2>
<a class="abs btn btn-join">JOIN NOW</a>
<div class="abs list-toggle"><span></span><span></span><span></span></div>
<a class="abs btn btn-share">SHARE</a>

<article class="abs tile" style="left:120px">
  <div class="tile-media" role="img" aria-label="Rugged mountain landscape" style="background:linear-gradient(180deg,#9fd0b8 0%,#5f7f86 50%,#3e4f6a 100%)"></div>
  <div class="tile-label">Vniqus Adventurs</div>
</article>
<article class="abs tile" style="left:354px">
  <div class="tile-media" role="img" aria-label="Couple silhouetted at sunset near a tower" style="background:linear-gradient(135deg,#c2401a 0%,#f0925a 50%,#f7d9e6 100%)"></div>
  <div class="tile-label">Romantic</div>
</article>
<article class="abs tile" style="left:589px">
  <div class="tile-media" role="img" aria-label="Smiling wedding couple" style="background:linear-gradient(180deg,#eef3f6 0%,#d9c7b2 60%,#8c8f96 100%)"></div>
  <div class="tile-label">Wedding</div>
</article>
<article class="abs tile" style="left:822px">
  <div class="tile-media" role="img" aria-label="Scuba diver swimming in blue water" style="background:linear-gradient(180deg,#2b8fd6 0%,#1462b3 60%,#0b3f86 100%)"></div>
  <div class="tile-label">Scuba</div>
</article>
<div class="abs slider-dots tiles-dots"><span></span><span class="active"></span><span></span><span></span></div>

</body>
</html>
```